Design an Elegant Handbag Brand website

I need a webiste design are looking for ideas for a new theme, color scheme, etc. You come up with the general look and feel of the home page and our team will take it from there.
We're only looking for a one (1) page layout which should be fashionable and graphic intensive, but also include the standard homepage links (about us, see our collections, etc)

Target Market(s)

Our customers are fashionable women looking for an animal friendly and environmentally friendly handbag.

Industry/Entity Type

Business

Number of Pages Required

1 page

Font styles to use
Serif
Sans Serif

Requirements
Must have
• Feel free to modify it with different colors or tweaks as you see fit. We are open to all suggestions.
Nice to have

```html
<!DOCTYPE html>
<html lang="en">
<head>
<meta charset="UTF-8">
<title>Look Be Stylish – Handbags</title>
<link rel="stylesheet" href="https://fonts.googleapis.com/css2?family=Roboto+Condensed:wght@400;500;700&family=Roboto:wght@500;700&display=swap">
<style>
  :root {
    --magenta: #c8237f;
    --slate: #5e5e5e;
    --blush-top: #f4e3e7;
    --blush-mid: #f0c3d2;
    --rose: #d5699a;
    --plum: #6a3b6a;
    --white: #ffffff;
    --beige: #c9b39a;
    --ink: #111111;
  }
  * { margin: 0; padding: 0; box-sizing: border-box; }
  html, body { width: 1200px; height: 853px; overflow: hidden; }
  body { font-family: "Roboto Condensed", Arial, sans-serif; }

  .hero {
    position: relative;
    width: 1200px;
    height: 853px;
    overflow: hidden;
    background: var(--blush-top);
  }
  .hero__backdrop {
    position: absolute; inset: 0;
    background:
      radial-gradient(circle at 550px 255px, rgba(255,255,255,0.95) 0, rgba(255,255,255,0.55) 50px, rgba(255,255,255,0) 150px),
      radial-gradient(ellipse 700px 380px at 1000px 760px, rgba(213,105,154,0.85), rgba(213,105,154,0) 100%),
      radial-gradient(ellipse 620px 300px at 420px 880px, rgba(106,59,106,0.95), rgba(106,59,106,0) 100%),
      linear-gradient(180deg, var(--blush-top) 0%, #f2d6de 40%, var(--blush-mid) 62%, #d98fb2 82%, #b4588d 100%);
  }

  .product-card {
    position: absolute;
    left: -30px; top: 48px;
    width: 460px; height: 745px;
    background: var(--white);
    border-radius: 24px;
    filter: blur(10px);
  }
  .product-card__photo {
    position: absolute;
    left: 0; top: 183px;
    width: 421px; height: 384px;
    background: radial-gradient(ellipse 190px 150px at 215px 190px, var(--beige) 0, #dccab6 60%, #ffffff 100%);
  }
  .carousel-dots {
    position: absolute;
    left: 160px; top: 672px;
    display: flex; align-items: center; gap: 9px;
  }
  .carousel-dots__dot { width: 10px; height: 10px; border-radius: 50%; background: var(--ink); }
  .carousel-dots__dot--active { width: 19px; height: 19px; background: transparent; border: 3px solid var(--ink); }

  .site-nav {
    position: absolute; top: 33px; right: 58px;
    display: flex; align-items: center;
  }
  .site-nav__search { width: 30px; height: 30px; margin-right: 26px; margin-top: 8px; }
  .site-nav__cart { display: flex; align-items: center; margin-right: 24px; margin-top: 4px; }
  .site-nav__cart-icon { width: 37px; height: 32px; margin-right: 8px; }
  .site-nav__cart-label { color: var(--magenta); font-weight: 500; font-size: 21px; letter-spacing: 0.3px; margin-right: 7px; }
  .site-nav__cart-count {
    width: 26px; height: 26px; border-radius: 50%;
    background: var(--white); color: var(--magenta);
    font-family: "Roboto", Arial, sans-serif; font-weight: 500; font-size: 16px;
    display: flex; align-items: center; justify-content: center;
  }
  .site-nav__menu { width: 50px; height: 30px; }

  .headline { position: absolute; left: 0; top: 0; }
  .headline__small {
    position: absolute;
    color: var(--slate);
    font-weight: 500;
    font-size: 82px;
    line-height: 1;
    letter-spacing: -2px;
  }
  .headline__small--look { left: 452px; top: 296px; }
  .headline__small--be { left: 504px; top: 365px; }
  .headline__big {
    position: absolute;
    left: 656px; top: 296px;
    color: var(--magenta);
    font-weight: 700;
    font-size: 146px;
    line-height: 1;
    letter-spacing: -1px;
  }

  .shop-button {
    position: absolute;
    left: 662px; top: 565px;
    width: 313px; height: 47px;
    border-radius: 24px;
    background: linear-gradient(90deg, rgba(232,140,180,0.75), rgba(244,190,214,0.75));
    border: 1.5px solid rgba(255,255,255,0.7);
    box-shadow: 0 2px 6px rgba(120,40,80,0.25);
    color: var(--white);
    font-family: "Roboto", Arial, sans-serif;
    font-weight: 700;
    font-size: 27px;
    word-spacing: 6px;
    display: flex; align-items: center; justify-content: center;
    padding-right: 10px;
    text-decoration: none;
  }
</style>
</head>
<body>
  <main class="hero">
    <div class="hero__backdrop" role="img" aria-label="Soft-focus pink city skyline at sunrise"></div>

    <div class="product-card"></div>
    <div class="product-card__photo" role="img" aria-label="Set of three beige faux-leather handbags: tote with tassel, shoulder bag and chain clutch"></div>
    <div class="carousel-dots" aria-label="Slide 2 of 3">
      <span class="carousel-dots__dot"></span>
      <span class="carousel-dots__dot carousel-dots__dot--active"></span>
      <span class="carousel-dots__dot"></span>
    </div>

    <nav class="site-nav">
      <svg class="site-nav__search" viewBox="0 0 30 30" aria-label="Search">
        <circle cx="12" cy="12" r="8.5" fill="none" stroke="var(--magenta)" stroke-width="4"/>
        <line x1="18" y1="18" x2="27" y2="27" stroke="var(--magenta)" stroke-width="5" stroke-linecap="round"/>
      </svg>
      <div class="site-nav__cart">
        <svg class="site-nav__cart-icon" viewBox="0 0 37 32" aria-hidden="true">
          <g fill="none" stroke="var(--magenta)" stroke-width="2" stroke-linejoin="round">
            <path d="M1 2 H7 L11 22 H31"/>
            <path d="M8 6 H35 L32 18 H10.5"/>
            <path d="M15 6 L16 18 M22 6 L22 18 M29 6 L28 18 M9 12 H33.5"/>
            <circle cx="14" cy="27" r="2.6"/>
            <circle cx="28" cy="27" r="2.6"/>
          </g>
        </svg>
        <span class="site-nav__cart-label">CART</span>
        <span class="site-nav__cart-count">1</span>
      </div>
      <svg class="site-nav__menu" viewBox="0 0 50 30" aria-label="Menu">
        <g fill="var(--magenta)">
          <rect x="0" y="0" width="50" height="6" rx="3"/>
          <rect x="0" y="12" width="50" height="6" rx="3"/>
          <rect x="0" y="24" width="50" height="6" rx="3"/>
        </g>
      </svg>
    </nav>

    <h1 class="headline">
      <span class="headline__small headline__small--look">LOOK</span>
      <span class="headline__small headline__small--be">BE</span>
      <span class="headline__big">STYLISH</span>
    </h1>

    <a class="shop-button" href="#">SHOP BAG</a>
  </main>
</body>
</html>
```